Business Card for Multi-Brand Sportswear Company

We are looking for a business card which represents our company and the multiple brands within it.

The company: Kelvo Athletics (LTD)
The brands: Kelv, TaliMati, VerdantFlex, Grit and Grime

Employees using these cards would be representing Kelvo Athletics, rather than any of the individual brands. You will see a current design within the uploaded files, to give some inspiration. The actual text of the brands is not necessary, but the logos should be on there is some format.

Our creative minds on this are stretched, so we are looking for someone to make this their own, and show us what a good business card should look like.

We may like to get these printed with spot gloss, so keep that in mind with your designs.

www.kelvoathletics.co.uk

Industry/Entity Type

Business

Contact Information for Business Card

Tom Pennington-Hale
Operations Manager
(+44) 1632 960 417
Tom@kelvoathletics.co.uk
www.kelvoathletics.co.uk

Font styles to use
Sans Serif
Other font styles liked:
• Eurostile

Colors
ffffff

Requirements
Nice to have
• Dark (black) background

```html
<!DOCTYPE html>
<html lang="en">
<head>
<meta charset="utf-8">
<title>Kelvo Athletics – Business Card</title>
<link rel="stylesheet" href="https://fonts.googleapis.com/css2?family=Open+Sans:wght@400;600;700&display=swap">
<style>
  :root {
    --canvas: #ebebeb;
    --card-white: #ffffff;
    --card-black: #0d0d0d;
    --ink: #1a1a1a;
    --ink-soft: #555555;
    --accent: #e3222a;
    --silver: #cfcfcf;
    --badge-purple: #5f5466;
  }
  * { box-sizing: border-box; margin: 0; padding: 0; }
  html, body {
    width: 1200px; height: 900px; overflow: hidden;
    background: var(--canvas);
    font-family: "Open Sans", Arial, sans-serif;
  }
  .canvas {
    width: 1200px; height: 900px;
    display: flex; align-items: center; justify-content: center; gap: 48px;
  }
  .card {
    position: relative;
    width: 525px; height: 300px;
    box-shadow: 0 6px 18px rgba(0,0,0,0.12);
  }
  .card--front { background: var(--card-white); color: var(--ink); }
  .card--back { background: var(--card-black); color: #fff; }

  .holder { position: absolute; left: 30px; top: 28px; }
  .holder__name { color: var(--accent); font-weight: 700; font-size: 15px; line-height: 1.2; }
  .holder__role { color: var(--ink-soft); font-size: 11px; }

  .contact { position: absolute; left: 30px; top: 112px; list-style: none; }
  .contact__item {
    display: flex; align-items: center; gap: 8px;
    font-size: 11px; color: var(--ink-soft); line-height: 17px;
  }
  .contact__icon { width: 10px; height: 10px; fill: var(--accent); flex: none; }

  .wordmark { position: absolute; display: flex; align-items: center; gap: 8px; }
  .wordmark__dot { width: 12px; height: 12px; border-radius: 50%; background: var(--accent); flex: none; }
  .wordmark__text { font-weight: 700; letter-spacing: 1px; text-transform: uppercase; line-height: 1; }
  .wordmark__tag {
    display: block; font-size: 7px; letter-spacing: 3px; font-weight: 400;
    text-transform: uppercase; margin-top: 4px; text-align: right;
  }
  .card--front .wordmark { left: 205px; top: 120px; }
  .card--front .wordmark__text { font-size: 24px; color: var(--ink); }
  .card--front .wordmark__tag { color: var(--ink-soft); }

  .address {
    position: absolute; right: 30px; bottom: 28px;
    text-align: right; font-size: 11px; color: var(--ink-soft); line-height: 16px;
  }

  .card--back .wordmark { left: 150px; top: 92px; }
  .card--back .wordmark__text { font-size: 28px; color: #fff; }
  .card--back .wordmark__tag { color: var(--silver); }

  .brands {
    position: absolute; left: 28px; right: 28px; bottom: 36px;
    display: flex; align-items: center; justify-content: space-between;
  }
  .brand { display: flex; align-items: center; gap: 6px; font-size: 12px; font-weight: 600; color: var(--silver); }
  .brand__square { width: 22px; height: 16px; border-radius: 3px; background: var(--badge-purple); }
  .brand__square--red { background: var(--accent); }
  .brand__circle { width: 18px; height: 18px; border-radius: 50%; border: 1.5px solid #8a8a8a; }
</style>
</head>
<body>
<main class="canvas">

  <section class="card card--front" aria-label="Business card front">
    <div class="holder">
      <p class="holder__name">Dan Ellery</p>
      <p class="holder__role">Managing Director</p>
    </div>

    <ul class="contact">
      <li class="contact__item">
        <svg class="contact__icon" viewBox="0 0 10 10" aria-hidden="true"><path d="M2 0.5 L3.6 0.5 L4.2 2.8 L3 3.6 Q4 5.8 6.4 7 L7.2 5.8 L9.5 6.4 L9.5 8 Q9.5 9.5 8 9.5 Q0.5 9 0.5 2 Q0.5 0.5 2 0.5Z"/></svg>
        +44(0)1632 960417
      </li>
      <li class="contact__item">
        <svg class="contact__icon" viewBox="0 0 10 10" aria-hidden="true"><path d="M0.5 2 H9.5 V8 H0.5Z M0.5 2 L5 5.5 L9.5 2" fill="none" stroke="#e3222a" stroke-width="1.2"/></svg>
        dan@kelvoathletics.co.uk
      </li>
      <li class="contact__item">
        <svg class="contact__icon" viewBox="0 0 10 10" aria-hidden="true"><g fill="none" stroke="#e3222a" stroke-width="1"><circle cx="5" cy="5" r="4.3"/><ellipse cx="5" cy="5" rx="1.8" ry="4.3"/><path d="M0.7 5 H9.3"/></g></svg>
        www.kelvoathletics.co.uk
      </li>
    </ul>

    <div class="wordmark">
      <span class="wordmark__dot" aria-hidden="true"></span>
      <span class="wordmark__text">Kelvo Athletics<span class="wordmark__tag">Performance Wear</span></span>
    </div>

    <address class="address" style="font-style:normal">
      Ashby Yard, Kelmoor,<br>Ridlow, KL4 2PT
    </address>
  </section>

  <section class="card card--back" aria-label="Business card back">
    <div class="wordmark">
      <span class="wordmark__dot" aria-hidden="true"></span>
      <span class="wordmark__text">Kelvo Athletics<span class="wordmark__tag">Performance Wear</span></span>
    </div>

    <div class="brands">
      <span class="brand"><span class="brand__square" aria-hidden="true"></span>TaliMati</span>
      <span class="brand"><span class="brand__square brand__square--red" aria-hidden="true"></span>Grit and Grime</span>
      <span class="brand">Kelv</span>
      <span class="brand"><span class="brand__circle" aria-hidden="true"></span>VerdantFlex</span>
    </div>
  </section>

</main>
</body>
</html>
```